Bright Harbor Galas one stop event solution

A new event company base in Singapore.
Specialist in PARTIES & SPECIAL EVENTS
FULL EVENT ORGANIZERS

Bright Harbor Galas provide all events need ranging from small to large number of people who are looking for a different way of organizing their event. We have a team of talented experience people working in a team to make your event more memorable moments...
Updates

Project Deadline Extended Reason: Date line is to rush would like to give them more time and more time for me to think Added Sunday, August 2, 2015

Target Market(s)

Club
Embassy
Pubs
Organisation
Community Events
ETC

Industry/Entity Type

Entertainment Industry

Font styles to use
Script

Colors
000000
fec214

Requirements
Must have
• anything that related to entertainment and event...
Nice to have
• Must be in gold and black color for the theme... wording and graphic in gold while the base background will be black...
Should not have
• Non

```html
<!DOCTYPE html>
<html lang="en">
<head>
<meta charset="utf-8">
<title>Bright Harbor Galas</title>
<link href="https://fonts.googleapis.com/css2?family=Noto+Serif:wght@400;700&family=Open+Sans:wght@400;600;700&display=swap" rel="stylesheet">
<style>
:root{
  --gold:#fec214;
  --gold-dark:#c8940a;
  --black:#000000;
  --ink:#161616;
  --panel:#232323;
  --panel-light:#2e2e2e;
  --grey-bg:#e9e9e9;
  --card:#ffffff;
  --text:#555555;
  --muted:#8a8a8a;
  --line:#d6d6d6;
}
*{box-sizing:border-box;margin:0;padding:0}
html,body{width:748px;height:1200px;overflow:hidden;background:var(--grey-bg)}
body{font-family:"Open Sans",Arial,sans-serif;color:var(--text);position:relative}
.page{position:relative;width:748px;height:1200px;overflow:hidden}

/* header */
.site-header{position:absolute;left:0;top:0;width:748px;height:75px;background:linear-gradient(#2a2a2a,#111)}
.brand{position:absolute;left:22px;top:22px;display:flex;align-items:center;gap:8px}
.brand-dot{width:16px;height:16px;border-radius:50%;background:var(--gold)}
.brand-name{font-family:"Noto Serif",Georgia,serif;font-weight:700;font-size:15px;color:var(--gold)}
.main-nav{position:absolute;right:20px;top:0;display:flex;height:75px}
.main-nav a{display:block;width:72px;height:75px;line-height:82px;text-align:center;font-family:"Noto Serif",Georgia,serif;font-size:12px;color:#ddd;text-decoration:none}
.main-nav a.active{background:linear-gradient(var(--gold),var(--gold-dark));color:#222;height:60px;line-height:60px;margin-top:15px;width:62px;margin-right:8px}

/* hero */
.hero{position:absolute;left:0;top:75px;width:748px;height:300px;background:radial-gradient(ellipse at 40% 40%,#2c2c2c,#0d0d0d)}
.hero-frame{position:absolute;left:22px;top:36px;width:430px;height:252px;background:#3a3a3a;border-radius:6px;padding:8px}
.hero-photo{width:100%;height:100%;border-radius:3px;background:radial-gradient(ellipse at 45% 30%,#f3b23a 0%,#c2641a 25%,#5a2410 55%,#120806 90%)}
.hero-copy{position:absolute;left:478px;top:52px;width:245px}
.hero-title{font-family:"Noto Serif",Georgia,serif;font-size:17px;color:var(--gold);font-weight:400}
.hero-title b{font-weight:700}
.hero-text{margin-top:12px;font-size:9.5px;line-height:15px;color:#a5a5a5}
.btn-gold{display:inline-block;margin-top:14px;padding:5px 12px;font-size:9px;color:#222;background:linear-gradient(var(--gold),var(--gold-dark));border-radius:3px}

/* slider controls */
.slider-bar{position:absolute;left:0;top:375px;width:748px;height:24px;background:#dcdcdc;border-bottom:1px solid #c8c8c8}
.slider-arrow{position:absolute;top:3px;width:18px;height:18px}
.slider-arrow.prev{left:14px}.slider-arrow.next{right:14px}
.slider-dots{position:absolute;left:352px;top:9px;display:flex;gap:5px}
.slider-dots span{width:7px;height:7px;border-radius:50%;background:#777}
.slider-dots span.on{background:#333}

/* cards */
.services{position:absolute;left:0;top:450px;width:748px}
.card{position:absolute;top:0;width:212px;height:250px;background:var(--card);border:1px solid var(--line);border-radius:4px;padding:12px 14px}
.card:nth-child(1){left:25px}.card:nth-child(2){left:268px}.card:nth-child(3){left:511px}
.card h3{font-family:"Noto Serif",Georgia,serif;font-size:14px;font-weight:400;text-align:center;color:#333}
.card .sub{text-align:center;font-size:8.5px;color:var(--muted);margin-top:2px}
.card-photo{margin-top:10px;height:80px;border:4px solid #eee}
.card p{margin-top:10px;font-size:8.5px;line-height:13px;color:var(--muted)}
.photo-events{background:linear-gradient(#3a1a0c,#c9662a 55%,#7a3414)}
.photo-dj{background:linear-gradient(#1a1e5a,#5f63d8 45%,#c0b4f2 60%,#2b1e66)}
.photo-parties{background:linear-gradient(#2a0f48,#6a2fb0 50%,#9a4fe0 65%,#1c0a32)}

/* subscribe */
.subscribe{position:absolute;left:15px;top:735px;width:718px;height:62px;background:linear-gradient(#f8f8f8,#e4e4e4);border:1px solid #cfcfcf;border-radius:4px}
.subscribe h2{position:absolute;left:22px;top:18px;font-family:"Noto Serif",Georgia,serif;font-weight:400;font-size:18px;color:#333}
.btn-dark{position:absolute;right:20px;top:16px;width:122px;height:30px;background:linear-gradient(#4a4a4a,#222);border-radius:3px;color:#fff;font-size:10px;font-weight:700;line-height:30px;padding-left:14px}
.btn-dark svg{position:absolute;right:10px;top:8px}

/* footer intro */
.footer-intro{position:absolute;left:0;top:822px;width:748px;height:100px;background:#dcdcdc;border-top:1px solid #c9c9c9}
.footer-intro h2{position:absolute;left:20px;top:20px;width:150px;font-family:"Noto Serif",Georgia,serif;font-weight:400;font-size:18px;line-height:24px;color:#333}
.footer-intro p{position:absolute;left:245px;top:18px;width:480px;font-size:9px;line-height:14px;color:#666}

/* dark footer */
.footer-main{position:absolute;left:0;top:922px;width:748px;height:228px;background:var(--ink)}
.fcol{position:absolute;top:16px}
.fcol h4{font-family:"Noto Serif",Georgia,serif;font-weight:400;font-size:14px;color:#eee;padding-bottom:8px;border-bottom:1px solid #333;margin-bottom:12px}
.fcol h4 b{color:var(--gold);font-weight:400}
.col-why{left:16px;width:220px}
.col-news{left:262px;width:220px}
.col-testimonial{left:508px;width:224px}
.why-list{list-style:none}
.why-list li{display:flex;align-items:center;gap:8px;font-size:9px;color:#aaa;margin-bottom:10px}
.news-item{display:flex;gap:10px;margin-bottom:14px}
.news-thumb{width:46px;height:40px;flex:none;border:2px solid #333}
.thumb-a{background:linear-gradient(#5a2a10,#e08a2a)}
.thumb-b{background:linear-gradient(#2a1a50,#b04ad0)}
.news-item .date{font-size:9px;color:#ddd}
.news-item p{font-size:8px;line-height:12px;color:#999;margin-top:2px}
.news-item .more{font-size:8px;color:var(--gold);margin-top:2px}
.quote-box{background:var(--panel-light);border-radius:3px;padding:12px;display:flex;gap:10px;position:relative}
.quote-box p{font-size:8.5px;line-height:13px;color:#aaa}
.quote-box::after{content:"";position:absolute;left:22px;bottom:-10px;border:10px solid transparent;border-top-color:var(--panel-light);border-bottom:0}
.quote-by{margin-top:16px;font-size:8.5px;color:var(--gold);padding-left:12px}

/* bottom bar */
.footer-bar{position:absolute;left:0;top:1150px;width:748px;height:50px;background:#0a0a0a;border-top:1px solid #262626}
.footer-nav{position:absolute;left:16px;top:15px;display:flex;gap:18px;align-items:center}
.footer-nav a{font-size:9px;color:#aaa;text-decoration:none}
.footer-nav a.active{background:var(--gold);color:#222;padding:4px 9px;border-radius:2px}
.copyright{position:absolute;right:18px;top:19px;font-size:9px;color:#888}
</style>
</head>
<body>
<div class="page">

  <header class="site-header">
    <div class="brand"><span class="brand-dot"></span><span class="brand-name">Bright Harbor Galas</span></div>
    <nav class="main-nav">
      <a class="active" href="#">Home</a>
      <a href="#">Elements</a>
      <a href="#">Portfolio</a>
      <a href="#">Layouts</a>
      <a href="#">Purchase</a>
    </nav>
  </header>

  <section class="hero">
    <div class="hero-frame"><div class="hero-photo" role="img" aria-label="Concert crowd with raised hands under warm stage lights"></div></div>
    <div class="hero-copy">
      <h1 class="hero-title"><b>Project</b> Titlet</h1>
      <p class="hero-text">Bright Harbor Galas plans parties, launches and club nights across Singapore. Our crew handles lighting, stage, sound and guest flow so every moment of your evening runs smoothly from the first arrival to the final encore.</p>
      <span class="btn-gold">Learn more</span>
    </div>
  </section>

  <div class="slider-bar">
    <svg class="slider-arrow prev" viewBox="0 0 18 18"><circle cx="9" cy="9" r="8" fill="#fff" stroke="#aaa"/><path d="M10.5 5.5 7 9l3.5 3.5" fill="none" stroke="#555" stroke-width="1.6"/></svg>
    <div class="slider-dots"><span class="on"></span><span></span><span></span><span></span><span></span></div>
    <svg class="slider-arrow next" viewBox="0 0 18 18"><circle cx="9" cy="9" r="8" fill="#fff" stroke="#aaa"/><path d="M7.5 5.5 11 9l-3.5 3.5" fill="none" stroke="#555" stroke-width="1.6"/></svg>
  </div>

  <section class="services">
    <article class="card">
      <h3>Events</h3><div class="sub">Small to large gatherings</div>
      <div class="card-photo photo-events" role="img" aria-label="Warm-lit banquet hall set for an event"></div>
      <p>From intimate dinners to corporate launches, we shape every detail of your event with care, matching venue, décor and programme to the people you invite.</p>
    </article>
    <article class="card">
      <h3>DJ/Fests</h3><div class="sub">Club nights and festivals</div>
      <div class="card-photo photo-dj" role="img" aria-label="Festival crowd under blue and violet stage lights"></div>
      <p>Resident DJs and touring acts bring the right sound to pubs, clubs and open-air stages, backed by our own lighting and audio crew for every set.</p>
    </article>
    <article class="card">
      <h3>Parties &amp; Events</h3><div class="sub">Embassy and community galas</div>
      <div class="card-photo photo-parties" role="img" aria-label="Party venue glowing in purple lighting"></div>
      <p>Themed parties and special evenings for embassies, organisations and community groups, planned end to end so your guests remember the night long after.</p>
    </article>
  </section>

  <section class="subscribe">
    <h2>Subscribe for 12 months and get an extra 2 months free!</h2>
    <span class="btn-dark">SIGN UP NOW
      <svg width="14" height="14" viewBox="0 0 14 14"><circle cx="7" cy="7" r="7" fill="#fff"/><path d="M5.5 4 8.5 7l-3 3" fill="none" stroke="#222" stroke-width="1.6"/></svg>
    </span>
  </section>

  <section class="footer-intro">
    <h2>Additional Footer Example</h2>
    <p>We build events that feel different. Tell us the mood, the guest list and the date, and our planners will return a full proposal with venue options, entertainment and budget within one week.</p>
  </section>

  <footer class="footer-main">
    <div class="fcol col-why">
      <h4>Why <b>Chose Us</b></h4>
      <ul class="why-list">
        <li><svg width="10" height="10" viewBox="0 0 10 10"><path d="M1 5.5 4 8l5-6" fill="none" stroke="#fec214" stroke-width="1.8"/></svg>Over ten years in event staging</li>
        <li><svg width="10" height="10" viewBox="0 0 10 10"><path d="M1 5.5 4 8l5-6" fill="none" stroke="#fec214" stroke-width="1.8"/></svg>A dedicated planner for every client</li>
        <li><svg width="10" height="10" viewBox="0 0 10 10"><path d="M1 5.5 4 8l5-6" fill="none" stroke="#fec214" stroke-width="1.8"/></svg>Transparent quotes, no hidden fees</li>
        <li><svg width="10" height="10" viewBox="0 0 10 10"><path d="M1 5.5 4 8l5-6" fill="none" stroke="#fec214" stroke-width="1.8"/></svg>Late-night crews on standby</li>
        <li><svg width="10" height="10" viewBox="0 0 10 10"><path d="M1 5.5 4 8l5-6" fill="none" stroke="#fec214" stroke-width="1.8"/></svg>Full setup and teardown included</li>
      </ul>
    </div>
    <div class="fcol col-news">
      <h4>Latest <b>News</b></h4>
      <div class="news-item">
        <div class="news-thumb thumb-a" role="img" aria-label="Rooftop gala at dusk"></div>
        <div><div class="date">12 March 2015</div><p>Our rooftop gala series returns this spring with three new venues by the bay.</p><div class="more">Read more »</div></div>
      </div>
      <div class="news-item">
        <div class="news-thumb thumb-b" role="img" aria-label="Evening reception hall in purple light"></div>
        <div><div class="date">18 March 2015</div><p>Bookings for year-end embassy receptions are now open to all partner organisations.</p><div class="more">Read more »</div></div>
      </div>
    </div>
    <div class="fcol col-testimonial">
      <h4>Client <b>Testimonials</b></h4>
      <div class="quote-box">
        <svg width="22" height="18" viewBox="0 0 22 18" style="flex:none"><path d="M0 18V10C0 4 3 1 8 0l1 2C6 3 5 5 5 8h4v10zM12 18V10c0-6 3-9 8-10l1 2c-3 1-4 3-4 6h4v10z" fill="#fec214"/></svg>
        <p>Bright Harbor Galas turned our community night into the event of the year. Every detail was handled and our guests are still talking about it.</p>
      </div>
      <div class="quote-by">Mei Lin, Events Club</div>
    </div>
  </footer>

  <div class="footer-bar">
    <nav class="footer-nav">
      <a class="active" href="#">Home</a><a href="#">Elements</a><a href="#">Portfolio</a><a href="#">Pages</a><a href="#">Purchase</a>
    </nav>
    <div class="copyright">Copyright © Bright Harbor Galas</div>
  </div>

</div>
</body>
</html>
```